Blue Harbor Trophies & Awards Unique Business Card Design

Recently selected a new logo design and waiting to recieve print files. I've attached image for your review. We are a trophies and awards company that provides engraving on trophies, plaques, name plates, name tags, desk sets, medals, acrylics, and signage.

We are located in Monroe, Louisiana and provide this service with computerized & laser engraving equipment.

Target Market(s)

Corporate, Sport, Church, and Special Events

Industry/Entity Type

Business

Contact Information for Business Card

I'd like to see the following list on the card: Trophies, Plaques, Name Plates, Name Tags, Desk Sets, Medals, Certificates... this is accomplished with Computerized & Laser Engraving

Colors
0555a3
ec1f27
ffffff

Requirements
Must have
• I like either single or double sided. If a design can be created with a frosted card stock I'd consider single. Must be Red, White, and Blue. Dale Penrow - Owner, 415 W 9th Ave, Monroe, La 70384 office 318-555-2190 fax 318-555-2186 email: blueharbor@blueharbortrophyco.example, and website: www.blueharbortrophyco.example

```html
<!DOCTYPE html>
<html lang="en">
<head>
<meta charset="utf-8">
<title>Blue Harbor Trophies &amp; Awards – Business Card</title>
<link href="https://fonts.googleapis.com/css2?family=Arimo:wght@400&family=Tinos:wght@400;700&display=swap" rel="stylesheet">
<style>
  :root {
    --brand-blue: #0555a3;
    --brand-red: #ec1f27;
    --card-white: #ffffff;
    --backdrop: #e9eaec;
    --rule: rgba(255, 255, 255, 0.55);
  }
  html, body {
    margin: 0;
    padding: 0;
    width: 1200px;
    height: 1000px;
    overflow: hidden;
    background: var(--backdrop);
  }
  .canvas {
    position: relative;
    width: 1200px;
    height: 1000px;
  }
  .business-card {
    position: absolute;
    left: 100px;
    top: 213px;
    width: 1000px;
    height: 574px;
    background: var(--card-white);
    box-shadow: 0 10px 30px rgba(0, 0, 0, 0.18);
    overflow: hidden;
    font-family: "Tinos", "Times New Roman", serif;
  }
  .card-shapes {
    position: absolute;
    inset: 0;
  }
  .contact-panel {
    position: absolute;
    left: 0;
    top: 0;
    width: 320px;
    height: 574px;
    color: var(--card-white);
  }
  .owner-name,
  .owner-title {
    position: absolute;
    left: 0;
    width: 322px;
    margin: 0;
    text-align: center;
    font-size: 28px;
    font-weight: 400;
    line-height: 34px;
  }
  .owner-name { top: 86px; }
  .owner-title { top: 124px; }
  .owner-rule {
    position: absolute;
    top: 168px;
    left: 62px;
    width: 200px;
    height: 1px;
    background: var(--rule);
  }
  .address,
  .phones {
    position: absolute;
    left: 56px;
    margin: 0;
    font-family: "Arimo", Arial, sans-serif;
    font-size: 20px;
    line-height: 36px;
    font-style: normal;
  }
  .address { top: 196px; }
  .phones { top: 288px; line-height: 30px; }
  .web-links {
    position: absolute;
    left: 22px;
    top: 488px;
    margin: 0;
    font-size: 17px;
    line-height: 32px;
    white-space: nowrap;
  }
  .company-name {
    position: absolute;
    left: 400px;
    top: 206px;
    width: 560px;
    margin: 0;
    text-align: center;
    color: var(--brand-blue);
    font-weight: 700;
    font-size: 62px;
    line-height: 72px;
  }
</style>
</head>
<body>
<main class="canvas">
  <article class="business-card" aria-label="Blue Harbor Trophies &amp; Awards business card, front">
    <svg class="card-shapes" width="1000" height="574" viewBox="0 0 1000 574" aria-hidden="true">
      <path class="red-sweep" d="M0 0 H525 C430 150 362 330 345 574 H0 Z" fill="var(--brand-red)"/>
      <path class="blue-panel" d="M0 0 H362 C350 200 340 420 322 574 H0 Z" fill="var(--brand-blue)"/>
    </svg>

    <section class="contact-panel">
      <h1 class="owner-name">Dale Penrow</h1>
      <p class="owner-title">Owner</p>
      <div class="owner-rule"></div>
      <address class="address">415 W 9th Ave, Monroe,<br>La 70384</address>
      <p class="phones">Office 318-555-2190<br>Fax 318-555-2186</p>
      <p class="web-links">blueharbor@blueharbortrophyco.example<br>www.blueharbortrophyco.example</p>
    </section>

    <h2 class="company-name">Blue Harbor<br>Trophies &amp; Awards</h2>
  </article>
</main>
</body>
</html>
```